Detail Shop Business card design

i need a business card design for my new detailing company called 'Brenner's Detail Shop'. i want an all black and white design . simple, direct and to the point. i want the designer to choose a fitting font to match the logothe front should have logo, address, phone and email and the back side should have a slogan and text indicating that we offer services on anything including cars, trucks, motorcycles and RVs. slogan will read "we take pride in your ride"
maybe also very small on the back side the IG icon with Brenners_Detail_Shop

phone 482.615.7734
address 7384 E Harlow Ave
Spokane WA 99342
email: BrennersDetail@quorvail.com

Target Market(s)

all ages , auto enthusiasts

Industry/Entity Type

Automotive

Contact Information for Business Card

the front should have logo, address, phone and email and the back side should have a slogan and text indicating that we offer services on anything including cars, trucks, motorcycles and RVs. slogan will read "we take pride in your ride"

phone 482.615.7734
address 7384 E Harlow Ave
Spokane WA 99342

Colors
000000
ffffff

Requirements
Must have
• bold font and very simple design with good spacing
Nice to have
• anything creative from the designer indicating we service any types of vehicles
Should not have
• any colors ,

```html
<!DOCTYPE html>
<html lang="en">
<head>
<meta charset="utf-8">
<title>Brenner's Detail Shop — Business Card</title>
<link href="https://fonts.googleapis.com/css2?family=IBM+Plex+Mono:wght@400;700&display=swap" rel="stylesheet">
<style>
  :root {
    --backdrop: #c2b59b;
    --ink: #000000;
    --paper: #ffffff;
    --charcoal: #3a3a3c;
    --card-edge: #1a1a1a;
    --mono: "IBM Plex Mono", monospace;
  }
  * { box-sizing: border-box; margin: 0; padding: 0; }
  html, body { width: 1200px; height: 1200px; overflow: hidden; }
  body { background: var(--backdrop); font-family: var(--mono); position: relative; }

  .card { position: absolute; left: 197px; width: 838px; height: 479px; overflow: hidden; }
  .card--front { top: 93px; border: 1px solid var(--card-edge); display: flex; }
  .card--back { top: 642px; background: var(--charcoal); color: var(--paper); }

  .front-brand { width: 419px; height: 100%; background: var(--paper); position: relative; border-right: 1px solid var(--card-edge); }
  .front-contact { width: 419px; height: 100%; background: var(--charcoal); color: var(--paper); position: relative; }

  .brand-mark { position: absolute; left: 0; right: 0; display: flex; flex-direction: column; align-items: center; text-align: center; }
  .brand-mark__dot { width: 110px; height: 110px; border-radius: 50%; margin-bottom: 26px; }
  .brand-mark__name { font-weight: 700; font-size: 34px; line-height: 1.15; letter-spacing: 1px; }
  .front-brand .brand-mark { top: 82px; color: var(--ink); }
  .front-brand .brand-mark__dot { background: var(--ink); }
  .card--back .brand-mark { top: 52px; color: var(--paper); }
  .card--back .brand-mark__dot { background: var(--paper); }

  .contact-row { position: absolute; left: 24px; display: flex; align-items: center; gap: 26px; }
  .contact-row svg { flex: none; width: 52px; height: 52px; fill: var(--paper); }
  .contact-row__text { font-size: 25px; letter-spacing: 1.5px; line-height: 1.3; }
  .contact-row--phone { top: 88px; }
  .contact-row--address { top: 180px; }
  .contact-row--email { top: 290px; }
  .contact-row--email .contact-row__text { font-size: 18px; letter-spacing: 0.5px; }

  .faint-name { position: absolute; right: -30px; bottom: 30px; font-weight: 700; font-size: 46px; line-height: 1.1;
    color: var(--paper); opacity: 0.05; text-align: center; transform: rotate(0deg); }

  .slogan { position: absolute; top: 356px; left: 0; right: 0; text-align: center; font-size: 17px; letter-spacing: 3px; }
  .social { position: absolute; top: 434px; left: 0; right: 0; display: flex; justify-content: center; align-items: center; gap: 10px; font-size: 16px; letter-spacing: 2px; }
  .social__square { width: 26px; height: 26px; border: 2.5px solid var(--paper); border-radius: 6px; }
</style>
</head>
<body>

<section class="card card--front">
  <div class="front-brand">
    <div class="brand-mark">
      <span class="brand-mark__dot"></span>
      <p class="brand-mark__name">Brenner's<br>Detail Shop</p>
    </div>
  </div>

  <div class="front-contact">
    <p class="faint-name" aria-hidden="true">Brenner's<br>Detail Shop</p>

    <div class="contact-row contact-row--phone">
      <svg viewBox="0 0 52 52" aria-hidden="true">
        <path d="M6 20c0-8 9-12 20-12s20 4 20 12v4h-10v-5c-3-1-7-1.5-10-1.5s-7 .5-10 1.5v5H6z"/>
        <path d="M14 24h24l6 16H8z"/>
        <circle cx="26" cy="33" r="5" fill="#3a3a3c"/>
        <rect x="6" y="42" width="40" height="4"/>
      </svg>
      <p class="contact-row__text">482.615.7734</p>
    </div>

    <div class="contact-row contact-row--address">
      <svg viewBox="0 0 52 52" aria-hidden="true">
        <path d="M26 2c-8 0-14 6-14 14 0 10 14 24 14 24s14-14 14-24c0-8-6-14-14-14zm0 20a6 6 0 1 1 0-12 6 6 0 0 1 0 12z"/>
        <path d="M4 44c0-4 8-6 14-7l2 3c-6 1-12 2-12 4s8 4 18 4 18-2 18-4-6-3-12-4l2-3c6 1 14 3 14 7 0 5-11 7-22 7S4 49 4 44z"/>
      </svg>
      <p class="contact-row__text">7384 E Harlow Ave<br>Spokane WA 99342</p>
    </div>

    <div class="contact-row contact-row--email">
      <svg viewBox="0 0 52 52" aria-hidden="true">
        <path d="M4 22l22-18 22 18v26H4z"/>
        <path d="M8 26l18 13 18-13v19H8z" fill="#3a3a3c"/>
        <path d="M8 45l14-10 4 3 4-3 14 10z"/>
        <circle cx="26" cy="18" r="8" fill="#3a3a3c"/>
        <text x="26" y="23" text-anchor="middle" font-size="14" font-weight="700" fill="#ffffff" font-family="IBM Plex Mono, monospace">e</text>
      </svg>
      <p class="contact-row__text">BrennersDetail@quorvail.com</p>
    </div>
  </div>
</section>

<section class="card card--back">
  <div class="brand-mark">
    <span class="brand-mark__dot"></span>
    <p class="brand-mark__name">Brenner's<br>Detail Shop</p>
  </div>
  <p class="slogan">We take pride in your ride</p>
  <div class="social">
    <span class="social__square"></span>
    <span>Brenners_Detail_Shop</span>
  </div>
</section>

</body>
</html>
```